Organic lawn care

take the same sign as the mosquito sign, only instead of the mosquito image have the red circle and line cross out the text of "chemicals". Have the sign say "this lawn receives ORGANIC grass treatments" "instantly SAFE for people and pets"

Lawn Care

```html
<!DOCTYPE html>
<html lang="en">
<head>
<meta charset="utf-8">
<title>Organic Lawn Care Sign</title>
<link rel="stylesheet" href="https://fonts.googleapis.com/css2?family=Montserrat:wght@500;800&display=swap">
<style>
  :root {
    --band-green: #025e28;
    --sign-white: #ffffff;
    --ban-red: #e30613;
    --ink-black: #000000;
  }
  * { margin: 0; padding: 0; box-sizing: border-box; }
  html, body {
    width: 1200px;
    height: 1200px;
    overflow: hidden;
    background: var(--sign-white);
  }
  .sign {
    position: relative;
    width: 1200px;
    height: 1200px;
    font-family: "Montserrat", sans-serif;
  }
  .band {
    position: absolute;
    left: 0;
    width: 1200px;
    background: var(--band-green);
    color: var(--sign-white);
    font-weight: 500;
    text-align: center;
  }
  .band--top {
    top: 0;
    height: 222px;
    padding-top: 24px;
    font-size: 69px;
    line-height: 89px;
    letter-spacing: 0.5px;
  }
  .band--bottom {
    top: 982px;
    height: 218px;
    padding-top: 62px;
    font-size: 66px;
    line-height: 90px;
    letter-spacing: 0.5px;
  }
  .ban-panel {
    position: absolute;
    top: 222px;
    left: 0;
    width: 1200px;
    height: 760px;
  }
  .ban-word {
    font-family: "Montserrat", sans-serif;
    font-weight: 800;
    font-size: 164px;
    fill: var(--ink-black);
  }
  .ban-ring {
    fill: none;
    stroke: var(--ban-red);
    stroke-width: 40;
  }
  .ban-slash {
    stroke: var(--ban-red);
    stroke-width: 38;
  }
</style>
</head>
<body>
  <main class="sign">
    <header class="band band--top">
      <p>This lawn receives ORGANIC<br>grass treatments</p>
    </header>

    <svg class="ban-panel" viewBox="0 222 1200 760" aria-label="No chemicals">
      <defs>
        <clipPath id="ring-inside">
          <circle cx="594" cy="604" r="300"/>
        </clipPath>
      </defs>
      <text class="ban-word" x="110" y="657" textLength="972" lengthAdjust="spacingAndGlyphs">CHEMICALS</text>
      <circle class="ban-ring" cx="594" cy="604" r="308"/>
      <line class="ban-slash" x1="860" y1="338" x2="328" y2="870" clip-path="url(#ring-inside)"/>
    </svg>

    <footer class="band band--bottom">
      <p>Instantly SAFE for people and pets</p>
    </footer>
  </main>
</body>
</html>
```